Bref créative
Quiet Harbor Dental Urgent Clinic- Business Cards and Stationary
Quiet Harbor Dental Urgent Clinic
Professional
Peter Delacroix, Jr., DMD
Founder/ CEO
2718 Pellam Rd
Ste 412
Houston, TX 77291
1-855-GRIN-WELLS
petedx4@mailvane.example
www.GRINWELLS.example
we can see you now!
RED, WHITE AND BLUE
I Have raised the $$$$ for postcard fabrication as well. let's get it!
attached is the graphic concept i'd like to achieve with the postcard.

```html
<!DOCTYPE html>
<html lang="en">
<head>
<meta charset="utf-8">
<title>Quiet Harbor Dental Urgent Clinic – Stationery Set</title>
<link href="https://fonts.googleapis.com/css2?family=Cinzel:wght@700&family=Open+Sans:wght@400;600;700&display=swap" rel="stylesheet">
<style>
:root{
  --bg:#e9e6e1;
  --paper:#ffffff;
  --blue:#1f63b5;
  --blue-dark:#0c3d84;
  --blue-light:#5fa3e6;
  --red:#c8182e;
  --ink:#2a3a55;
  --faint:#e6edf6;
  --line:#b9c6d8;
}
*{margin:0;padding:0;box-sizing:border-box}
html,body{width:1200px;height:439px;overflow:hidden;background:var(--bg)}
body{position:relative;font-family:"Open Sans",sans-serif;color:var(--ink)}
.item{position:absolute;background:var(--paper);box-shadow:0 2px 6px rgba(0,0,0,.25);overflow:hidden}
.wave{position:absolute;left:0;bottom:0;width:100%;display:block}
.brand{position:absolute;display:flex;align-items:center;gap:4px;white-space:nowrap}
.brand-dot{flex:none;width:10px;height:10px;border-radius:50%;background:var(--blue)}
.brand-name{font-family:"Cinzel",serif;font-weight:700;color:var(--blue-dark);font-size:8px;letter-spacing:.3px;line-height:1.1}
.brand-sub{font-size:5px;color:var(--ink)}
.watermark{position:absolute;border-radius:50%;background:var(--faint)}
.footer-text{position:absolute;left:0;width:100%;text-align:center;font-size:3.6px;color:#fff;white-space:nowrap}

/* folder */
.folder{position:absolute;left:19px;top:12px;width:241px;height:420px}
.folder svg{width:100%;height:100%;display:block;filter:drop-shadow(0 2px 4px rgba(0,0,0,.3))}
.cover-brand{left:8px;top:146px}
.cover-brand .brand-dot{width:12px;height:12px;background:var(--paper)}
.cover-brand .brand-name{color:#fff;font-size:10px}
.cover-brand .brand-sub{color:#fff;font-size:5.5px}
.inside-brand{left:128px;top:20px}
.inside-brand .brand-name{font-size:7px}
.inside-brand .brand-sub{font-size:4.5px}
.pocket-brand{top:380px}
.pocket-brand .brand-dot{width:7px;height:7px;background:#fff}
.pocket-brand .brand-name{font-size:6px;color:#fff}

/* invoice */
.invoice{left:276px;top:96px;width:157px;height:336px}
.invoice .brand{left:50px;top:10px}
.invoice-table{position:absolute;left:14px;top:40px;width:128px;border-collapse:collapse;font-size:3.6px}
.invoice-table th{background:var(--blue);color:#fff;font-weight:600;padding:1px 2px;text-align:left}
.invoice-table td{border:0.5px solid var(--line);height:7px}
.pay-row{position:absolute;left:14px;top:112px;display:flex;gap:10px;font-size:3.6px;white-space:nowrap}
.pay-row span::before{content:"";display:inline-block;width:3px;height:3px;border:.5px solid var(--ink);margin-right:2px}

/* letterhead */
.letterhead{left:451px;top:96px;width:164px;height:336px}
.letterhead .brand{left:52px;top:10px}

/* cards */
.card{width:98px;height:65px}
.card-photo{left:492px;top:19px}
.photo{position:absolute;left:6px;top:6px;width:36px;height:46px;background:linear-gradient(160deg,#c9d2dc,#8e9aa8)}
.card-photo .person{position:absolute;left:46px;top:14px;font-size:3.8px;font-weight:700;color:var(--blue-dark);white-space:nowrap}
.card-photo .role{position:absolute;left:46px;top:20px;font-size:3.6px;white-space:nowrap}
.card-photo .contact{position:absolute;left:46px;top:28px;font-size:3.3px;line-height:1.35;white-space:nowrap}
.card-front{left:619px;top:19px}
.card-front .brand{left:20px;top:12px}
.card-small{width:86px;height:40px;top:67px}
.card-small .brand-dot{width:8px;height:8px}
.card-small .brand-name{font-size:6.5px}
.card-white{left:737px}
.card-white .brand{left:8px;top:8px}
.card-blue{left:826px;background:linear-gradient(160deg,var(--blue),var(--blue-dark))}
.card-blue .brand{left:8px;top:15px}
.card-blue .brand-dot{background:#fff}
.card-blue .brand-name{color:#fff}

/* notecard */
.notecard{left:732px;top:139px;width:216px;height:125px}
.notecard .brand{left:68px;top:48px}
.notecard .brand-name{font-size:10px}

/* envelope */
.envelope{left:732px;top:283px;width:216px;height:137px}
.envelope .flap{position:absolute;left:0;top:0;width:100%;height:70px}
.envelope .brand{left:80px;top:76px}
.envelope .tagline{position:absolute;left:0;width:100%;top:94px;text-align:center;font-size:4.4px;color:var(--blue-dark);font-weight:600}
</style>
</head>
<body>

<!-- presentation folder -->
<div class="folder">
  <svg viewBox="0 0 241 420" preserveAspectRatio="none">
    <defs>
      <linearGradient id="coverGrad" x1="0" y1="0" x2="1" y2="1">
        <stop offset="0" stop-color="#3c86d4"/>
        <stop offset="1" stop-color="#0c3d84"/>
      </linearGradient>
    </defs>
    <rect x="0" y="0" width="121" height="216" fill="url(#coverGrad)"/>
    <path d="M0 60 Q60 20 121 70" stroke="#fff" stroke-opacity=".35" stroke-width="3" fill="none"/>
    <circle cx="60" cy="90" r="40" fill="#fff" fill-opacity=".08"/>
    <rect x="121" y="0" width="120" height="216" fill="#fff"/>
    <path d="M121 150 Q180 110 241 130 V216 H121Z" fill="#eef2f8"/>
    <path d="M0 216 H241 V420 H150 L121 250 L92 420 H0Z" fill="#fff"/>
    <path d="M0 360 Q50 345 100 362 L92 420 H0Z" fill="#1f63b5"/>
    <path d="M0 356 Q50 341 100 358" stroke="#c8182e" stroke-width="2" fill="none"/>
    <path d="M145 362 Q195 345 241 360 V420 H150Z" fill="#1f63b5"/>
    <path d="M144 358 Q195 341 241 356" stroke="#c8182e" stroke-width="2" fill="none"/>
    <line x1="121" y1="216" x2="121" y2="250" stroke="#c9d2de" stroke-width=".6"/>
  </svg>
  <div class="brand cover-brand"><span class="brand-dot"></span><div><div class="brand-name">QUIET HARBOR</div><div class="brand-sub">Dental Urgent Clinic</div></div></div>
  <div class="brand inside-brand"><span class="brand-dot"></span><div><div class="brand-name">QUIET HARBOR</div><div class="brand-sub">Dental Urgent Clinic</div></div></div>
  <div class="brand pocket-brand" style="left:24px"><span class="brand-dot"></span><span class="brand-name">QUIET HARBOR</span></div>
  <div class="brand pocket-brand" style="left:166px"><span class="brand-dot"></span><span class="brand-name">QUIET HARBOR</span></div>
</div>

<!-- invoice sheet -->
<div class="item invoice">
  <div class="brand"><span class="brand-dot"></span><div><div class="brand-name">QUIET HARBOR</div><div class="brand-sub">Dental Urgent Clinic</div></div></div>
  <table class="invoice-table">
    <tr><th>Description</th><th>Qty</th><th>Amount</th></tr>
    <tr><td></td><td></td><td></td></tr>
    <tr><td></td><td></td><td></td></tr>
    <tr><td></td><td></td><td></td></tr>
    <tr><td></td><td></td><td></td></tr>
    <tr><td></td><td></td><td></td></tr>
    <tr><td></td><td></td><td></td></tr>
    <tr><td></td><td></td><td></td></tr>
  </table>
  <div class="pay-row"><span>Cash</span><span>Check</span><span>Card</span><span>Insurance</span><span>Other</span></div>
  <div class="watermark" style="left:38px;top:160px;width:80px;height:80px"></div>
  <svg class="wave" viewBox="0 0 100 22" preserveAspectRatio="none" style="height:44px">
    <path d="M0 9 Q50 -2 100 9 V22 H0Z" fill="var(--blue)"/>
    <path d="M0 7 Q50 -4 100 7" stroke="var(--red)" stroke-width="1.2" fill="none"/>
  </svg>
  <div class="footer-text" style="bottom:8px">2718 Pellam Rd, Ste 412, Houston, TX 77291 · 1-855-GRIN-WELLS</div>
</div>

<!-- letterhead -->
<div class="item letterhead">
  <div class="brand"><span class="brand-dot"></span><div><div class="brand-name">QUIET HARBOR</div><div class="brand-sub">Dental Urgent Clinic</div></div></div>
  <div class="watermark" style="left:37px;top:130px;width:90px;height:90px"></div>
  <svg class="wave" viewBox="0 0 100 22" preserveAspectRatio="none" style="height:44px">
    <path d="M0 9 Q50 -2 100 9 V22 H0Z" fill="var(--blue)"/>
    <path d="M0 7 Q50 -4 100 7" stroke="var(--red)" stroke-width="1.2" fill="none"/>
  </svg>
  <div class="footer-text" style="bottom:8px">2718 Pellam Rd, Ste 412, Houston, TX 77291 · www.GRINWELLS.example</div>
</div>

<!-- business card, back with portrait -->
<div class="item card card-photo">
  <div class="photo" role="img" aria-label="Portrait photograph of the dentist"></div>
  <div class="person">Peter Delacroix, Jr., DMD</div>
  <div class="role">Founder/ CEO</div>
  <div class="contact">1-855-GRIN-WELLS<br>petedx4@mailvane.example<br>www.GRINWELLS.example</div>
  <svg class="wave" viewBox="0 0 100 12" preserveAspectRatio="none" style="height:9px">
    <path d="M0 6 Q50 0 100 6 V12 H0Z" fill="var(--blue)"/>
  </svg>
</div>

<!-- business card, front -->
<div class="item card card-front">
  <div class="brand"><span class="brand-dot"></span><div><div class="brand-name">QUIET HARBOR</div><div class="brand-sub">Dental Urgent Clinic</div></div></div>
  <svg class="wave" viewBox="0 0 100 22" preserveAspectRatio="none" style="height:22px">
    <path d="M0 10 Q50 0 100 10 V22 H0Z" fill="var(--blue)"/>
    <path d="M0 8 Q50 -2 100 8" stroke="var(--red)" stroke-width="1.4" fill="none"/>
  </svg>
</div>

<!-- small cards -->
<div class="item card-small card-white">
  <div class="brand"><span class="brand-dot"></span><span class="brand-name">QUIET HARBOR</span></div>
  <svg class="wave" viewBox="0 0 100 20" preserveAspectRatio="none" style="height:14px">
    <path d="M0 10 Q50 0 100 10 V20 H0Z" fill="var(--blue)"/>
    <path d="M0 8 Q50 -2 100 8" stroke="var(--red)" stroke-width="1.4" fill="none"/>
  </svg>
</div>
<div class="item card-small card-blue">
  <div class="brand"><span class="brand-dot"></span><span class="brand-name">QUIET HARBOR</span></div>
</div>

<!-- notecard -->
<div class="item notecard">
  <div class="brand"><span class="brand-dot"></span><div><div class="brand-name">QUIET HARBOR</div><div class="brand-sub">Dental Urgent Clinic</div></div></div>
  <svg class="wave" viewBox="0 0 100 22" preserveAspectRatio="none" style="height:30px">
    <path d="M0 10 Q50 0 100 10 V22 H0Z" fill="var(--blue)"/>
    <path d="M0 8 Q50 -2 100 8" stroke="var(--red)" stroke-width="1.2" fill="none"/>
  </svg>
</div>

<!-- envelope -->
<div class="item envelope">
  <svg class="flap" viewBox="0 0 216 70" preserveAspectRatio="none">
    <path d="M0 0 L108 66 L216 0" fill="#f3f6fa" stroke="var(--blue)" stroke-width="2"/>
  </svg>
  <div class="brand"><span class="brand-dot"></span><span class="brand-name">QUIET HARBOR</span></div>
  <div class="tagline">we can see you now!</div>
  <svg class="wave" viewBox="0 0 100 22" preserveAspectRatio="none" style="height:26px">
    <path d="M0 10 Q50 0 100 10 V22 H0Z" fill="var(--blue)"/>
    <path d="M0 8 Q50 -2 100 8" stroke="var(--red)" stroke-width="1.2" fill="none"/>
  </svg>
</div>

</body>
</html>
```